Company Eco-System 1 Page Graphic

We need a 1 page visual of what our company does and all of the different parts of the company and what they do.
We would like it to be as simple as possible, modern, clean.
Our logo and colour palette are attached.
We are an events management company and we want to show our shareholders a graphic that demonstrates how the different parts of our company work together to deliver events and our strategic goals

Target Market(s)

Our local Council which we are owned by

Industry/Entity Type

Events Management

Font styles to use
Other font styles liked:
• Calibri light

```html
<!DOCTYPE html>
<html lang="en">
<head>
<meta charset="utf-8">
<title>Company Eco-System</title>
<link href="https://fonts.googleapis.com/css2?family=Open+Sans:wght@400;600;700&display=swap" rel="stylesheet">
<style>
  :root{
    --ink:#111111;
    --paper:#ffffff;
    --attraction:#80c68e;
    --delivery:#c34a3e;
    --planning:#235b4f;
    --commercial:#f6ca46;
    --gold:#f0b93a;
    --marketing:#6a2730;
    --assets:#f9dde6;
    --assets-arrow:#f3c4d3;
    --assets-ink:#2f2326;
    --people:#dd3a44;
    --systems:#441748;
    --events:#3f5ea9;
    --core:#60398f;
  }
  html,body{margin:0;padding:0;width:1200px;height:927px;overflow:hidden;background:var(--paper);}
  svg{display:block;font-family:"Open Sans",Arial,sans-serif;}
  .brand{font-weight:700;font-size:34px;fill:var(--ink);}
  .brand-dot{fill:var(--ink);}
  .frame{fill:none;stroke:var(--ink);stroke-width:3;}
  .divider{stroke:var(--ink);stroke-width:3;}
  .pillar{font-weight:700;font-size:26px;fill:var(--ink);}
  .item{stroke:var(--paper);stroke-width:3;}
  .item-sep{stroke:var(--assets-ink);stroke-width:1.5;}
  .item-label{font-size:15px;fill:var(--paper);}
  .item-label.dark{fill:var(--assets-ink);}
  .wedge{stroke:var(--paper);stroke-width:12;stroke-linejoin:miter;}
  .wedge-label{font-weight:700;font-size:16.5px;fill:var(--paper);text-anchor:middle;dominant-baseline:central;}
  .wedge-label.dark{fill:var(--ink);}
  .bracket{fill:none;stroke-width:4;}
  .ticks{fill:none;stroke-width:12;}
  .ring{fill:none;stroke:var(--ink);stroke-width:2;}
  .ring-label{font-weight:700;font-size:15px;fill:var(--ink);}
  .core-label{font-weight:700;font-size:15px;fill:var(--paper);text-anchor:middle;dominant-baseline:central;}
  .events-label{font-weight:700;font-size:23px;fill:var(--paper);text-anchor:middle;}
  .f-attraction{fill:var(--attraction);} .s-attraction{stroke:var(--attraction);}
  .f-delivery{fill:var(--delivery);} .s-delivery{stroke:var(--delivery);}
  .f-planning{fill:var(--planning);} .s-planning{stroke:var(--planning);}
  .f-commercial{fill:var(--commercial);} .s-commercial{stroke:var(--commercial);}
  .f-marketing{fill:var(--marketing);} .s-marketing{stroke:var(--marketing);}
  .f-assets{fill:var(--assets);} .s-assets{stroke:var(--assets);}
  .f-people{fill:var(--people);} .s-people{stroke:var(--people);}
  .f-systems{fill:var(--systems);} .s-systems{stroke:var(--systems);}
  .f-gold{fill:var(--gold);} .f-assets-arrow{fill:var(--assets-arrow);}
</style>
</head>
<body>
<svg width="1200" height="927" viewBox="0 0 1800 1390" xmlns="http://www.w3.org/2000/svg">
  <defs>
    <path id="cell-attraction" d="M351.61,-16.54 L602.34,-28.33 A603 603 0 0 1 602.34,28.33 L351.61,16.54 A352 352 0 0 0 351.61,-16.54 Z"/>
    <path id="cell-delivery" d="M351.55,-17.81 L602.23,-30.51 A603 603 0 0 1 602.23,30.51 L351.55,17.81 A352 352 0 0 0 351.55,-17.81 Z"/>
    <path id="cell-planning" d="M351.58,-17.27 L602.28,-29.59 A603 603 0 0 1 602.28,29.59 L351.58,17.27 A352 352 0 0 0 351.58,-17.27 Z"/>
    <path id="cell-commercial" d="M351.52,-18.42 L602.17,-31.56 A603 603 0 0 1 602.17,31.56 L351.52,18.42 A352 352 0 0 0 351.52,-18.42 Z"/>
    <path id="cell-marketing" d="M351.63,-16.12 L602.37,-27.62 A603 603 0 0 1 602.37,27.62 L351.63,16.12 A352 352 0 0 0 351.63,-16.12 Z"/>
    <path id="cell-assets" d="M350.66,-30.68 L600.70,-52.56 A603 603 0 0 1 600.70,52.56 L350.66,30.68 A352 352 0 0 0 350.66,-30.68 Z"/>
    <path id="cell-people" d="M350.79,-29.15 L600.93,-49.93 A603 603 0 0 1 600.93,49.93 L350.79,29.15 A352 352 0 0 0 350.79,-29.15 Z"/>
    <path id="cell-systems" d="M350.70,-30.24 L600.77,-51.81 A603 603 0 0 1 600.77,51.81 L350.70,30.24 A352 352 0 0 0 350.70,-30.24 Z"/>
    <path id="pillar-top" d="M-620,0 A620 620 0 0 1 620,0"/>
    <path id="pillar-bottom" d="M-647,0 A647 647 0 0 0 647,0"/>
    <path id="cycle-top" d="M-127,0 A127 127 0 0 1 127,0"/>
    <path id="cycle-bottom" d="M-127,0 A127 127 0 0 0 127,0"/>
    <path id="pointer" d="M140,0 L155,-9 L155,9 Z"/>
    <path id="cycle-arrow" d="M121,-5 L133,-5 L127,6 Z"/>
  </defs>

  <g class="brand-block">
    <circle class="brand-dot" cx="1376" cy="82" r="11"/>
    <text class="brand" x="1398" y="94">Harbourline Events</text>
  </g>

  <g class="wheel" transform="translate(900 690)">
    <circle class="frame" r="667"/>
    <line class="divider" x1="0" y1="-605" x2="0" y2="-667"/>
    <line class="divider" x1="605" y1="0" x2="667" y2="0"/>
    <line class="divider" x1="-605" y1="0" x2="-667" y2="0"/>
    <line class="divider" x1="-302.5" y1="523.9" x2="-333.5" y2="577.6"/>
    <line class="divider" x1="302.5" y1="523.9" x2="333.5" y2="577.6"/>

    <text class="pillar"><textPath href="#pillar-top" startOffset="27.2%" text-anchor="middle">CELEBRATE AND SOURCE LOCAL</textPath></text>
    <text class="pillar"><textPath href="#pillar-top" startOffset="76%" text-anchor="middle">STRATEGIC PARTNERSHIP</textPath></text>
    <text class="pillar" dy="19"><textPath href="#pillar-bottom" startOffset="16.7%" text-anchor="middle">ENVIRONMENTAL AND SOCIAL SUSTAINBILITY</textPath></text>
    <text class="pillar" dy="19"><textPath href="#pillar-bottom" startOffset="50%" text-anchor="middle">ENVIRONMENTAL AND SOCIAL SUSTAINBILITY</textPath></text>
    <text class="pillar" dy="19"><textPath href="#pillar-bottom" startOffset="83.3%" text-anchor="middle">STACKEHOLDERS MANAGEMENT</textPath></text>

    <!-- Event attraction sales -->
    <g class="group f-attraction">
      <use href="#cell-attraction" class="item" transform="rotate(-123.3)"/>
      <use href="#cell-attraction" class="item" transform="rotate(-117.9)"/>
      <use href="#cell-attraction" class="item" transform="rotate(-112.5)"/>
      <use href="#cell-attraction" class="item" transform="rotate(-107.2)"/>
      <use href="#cell-attraction" class="item" transform="rotate(-101.8)"/>
      <use href="#cell-attraction" class="item" transform="rotate(-96.4)"/>
      <use href="#cell-attraction" class="item" transform="rotate(-91)"/>
    </g>
    <g class="labels">
      <text class="item-label" transform="rotate(56.7)" x="-478" dy=".35em" text-anchor="middle">Technical Services</text>
      <text class="item-label" transform="rotate(62.1)" x="-478" dy=".35em" text-anchor="middle">Sport</text>
      <text class="item-label" transform="rotate(67.5)" x="-478" dy=".35em" text-anchor="middle">Business</text>
      <text class="item-label" transform="rotate(72.8)" x="-478" dy=".35em" text-anchor="middle">Education</text>
      <text class="item-label" transform="rotate(78.2)" x="-478" dy=".35em" text-anchor="middle">Lifestyle</text>
      <text class="item-label" transform="rotate(83.6)" x="-478" dy=".35em" text-anchor="middle">Community</text>
      <text class="item-label" transform="rotate(89)" x="-478" dy=".35em" text-anchor="middle">Entertainment</text>
    </g>

    <!-- Event delivery / operations -->
    <g class="group f-delivery">
      <use href="#cell-delivery" class="item" transform="rotate(-83.7)"/>
      <use href="#cell-delivery" class="item" transform="rotate(-77.9)"/>
      <use href="#cell-delivery" class="item" transform="rotate(-72.1)"/>
      <use href="#cell-delivery" class="item" transform="rotate(-66.3)"/>
      <use href="#cell-delivery" class="item" transform="rotate(-60.5)"/>
      <use href="#cell-delivery" class="item" transform="rotate(-54.7)"/>
      <use href="#cell-delivery" class="item" transform="rotate(-48.9)"/>
    </g>
    <g class="labels">
      <text class="item-label" transform="rotate(-83.7)" x="478" dy=".35em" text-anchor="middle">Procurement</text>
      <text class="item-label" transform="rotate(-77.9)" x="478" dy=".35em" text-anchor="middle">Client Engagement</text>
      <text class="item-label" transform="rotate(-72.1)" x="478" dy=".35em" text-anchor="middle">Health and Safety</text>
      <text class="item-label" transform="rotate(-66.3)" x="478" dy=".35em" text-anchor="middle">Event Logistics</text>
      <text class="item-label" transform="rotate(-60.5)" x="478" dy=".35em" text-anchor="middle">Resourcing</text>
      <text class="item-label" transform="rotate(-54.7)" x="478" dy=".35em" text-anchor="middle">Retail Menu Design</text>
      <text class="item-label" transform="rotate(-48.9)" x="478" dy=".35em" text-anchor="middle">Corporate Menu Design</text>
    </g>

    <!-- Event planning management -->
    <g class="group f-planning">
      <use href="#cell-planning" class="item" transform="rotate(-42.2)"/>
      <use href="#cell-planning" class="item" transform="rotate(-36.6)"/>
      <use href="#cell-planning" class="item" transform="rotate(-30.9)"/>
      <use href="#cell-planning" class="item" transform="rotate(-25.3)"/>
      <use href="#cell-planning" class="item" transform="rotate(-19.7)"/>
      <use href="#cell-planning" class="item" transform="rotate(-14.1)"/>
      <use href="#cell-planning" class="item" transform="rotate(-8.4)"/>
      <use href="#cell-planning" class="item" transform="rotate(-2.8)"/>
    </g>
    <g class="labels">
      <text class="item-label" transform="rotate(-42.2)" x="478" dy=".35em" text-anchor="middle">Retail Foods and Beverage</text>
      <text class="item-label" transform="rotate(-36.6)" x="478" dy=".35em" text-anchor="middle">Corporate Food and Beverage</text>
      <text class="item-label" transform="rotate(-30.9)" x="478" dy=".35em" text-anchor="middle">Emergency Management</text>
      <text class="item-label" transform="rotate(-25.3)" x="478" dy=".35em" text-anchor="middle">Hosting</text>
      <text class="item-label" transform="rotate(-19.7)" x="478" dy=".35em" text-anchor="middle">Kitchen Operations</text>
      <text class="item-label" transform="rotate(-14.1)" x="478" dy=".35em" text-anchor="middle">Venue Management</text>
      <text class="item-label" transform="rotate(-8.4)" x="478" dy=".35em" text-anchor="middle">Cleaning</text>
      <text class="item-label" transform="rotate(-2.8)" x="478" dy=".35em" text-anchor="middle">Traffic Management + Car Pricing</text>
    </g>

    <!-- Commercial -->
    <g class="group f-commercial">
      <use href="#cell-commercial" class="item" transform="rotate(-131)"/>
      <use href="#cell-commercial" class="item" transform="rotate(-137)"/>
      <use href="#cell-commercial" class="item" transform="rotate(-143)"/>
      <use href="#cell-commercial" class="item" transform="rotate(-149)"/>
      <use href="#cell-commercial" class="item" transform="rotate(-155)"/>
    </g>
    <g class="labels">
      <text class="item-label dark" transform="rotate(49)" x="-478" dy=".35em" text-anchor="middle">Commercial Partnership</text>
      <text class="item-label dark" transform="rotate(43)" x="-478" dy=".35em" text-anchor="middle">Sponsorship</text>
      <text class="item-label dark" transform="rotate(37)" x="-478" dy=".35em" text-anchor="middle">Revenue Growth</text>
      <text class="item-label dark" transform="rotate(31)" x="-478" dy=".35em" text-anchor="middle">Ticketing</text>
      <text class="item-label dark" transform="rotate(25)" x="-478" dy=".35em" text-anchor="middle">Membership</text>
    </g>

    <!-- Marketing and communications -->
    <g class="group f-marketing">
      <use href="#cell-marketing" class="item" transform="rotate(-161.6)"/>
      <use href="#cell-marketing" class="item" transform="rotate(-166.9)"/>
      <use href="#cell-marketing" class="item" transform="rotate(-172.1)"/>
      <use href="#cell-marketing" class="item" transform="rotate(-177.4)"/>
    </g>
    <g class="labels">
      <text class="item-label" transform="rotate(18.4)" x="-478" dy=".35em" text-anchor="middle">Brand</text>
      <text class="item-label" transform="rotate(13.1)" x="-478" dy=".35em" text-anchor="middle">Reputation</text>
      <text class="item-label" transform="rotate(7.9)" x="-478" dy=".35em" text-anchor="middle">Public Relation</text>
      <text class="item-label" transform="rotate(2.6)" x="-478" dy=".35em" text-anchor="middle">Engagement</text>
    </g>

    <!-- Assets and facilities -->
    <g class="group f-assets">
      <use href="#cell-assets" class="item" transform="rotate(-185)"/>
      <use href="#cell-assets" class="item" transform="rotate(-195)"/>
      <use href="#cell-assets" class="item" transform="rotate(-205)"/>
      <use href="#cell-assets" class="item" transform="rotate(-215)"/>
      <use href="#cell-assets" class="item" transform="rotate(-225)"/>
    </g>
    <g class="separators">
      <line class="item-sep" x1="352" y1="0" x2="603" y2="0" transform="rotate(-190)"/>
      <line class="item-sep" x1="352" y1="0" x2="603" y2="0" transform="rotate(-200)"/>
      <line class="item-sep" x1="352" y1="0" x2="603" y2="0" transform="rotate(-210)"/>
      <line class="item-sep" x1="352" y1="0" x2="603" y2="0" transform="rotate(-220)"/>
    </g>
    <g class="labels">
      <text class="item-label dark" transform="rotate(-5)" x="-478" dy=".35em" text-anchor="middle">Reactive Maintenance</text>
      <text class="item-label dark" transform="rotate(-15)" x="-478" dy=".35em" text-anchor="middle">Preventative Maintenance</text>
      <text class="item-label dark" transform="rotate(-25)" x="-478" dy=".35em" text-anchor="middle">Capital Programme</text>
      <text class="item-label dark" transform="rotate(-35)" x="-478" dy=".35em" text-anchor="middle">Venue Presentation</text>
      <text class="item-label dark" transform="rotate(-45)" x="-478" dy=".35em" text-anchor="middle">Event Day Response</text>
    </g>

    <!-- People and culture -->
    <g class="group f-people">
      <use href="#cell-people" class="item" transform="rotate(-236.75)"/>
      <use href="#cell-people" class="item" transform="rotate(-246.25)"/>
      <use href="#cell-people" class="item" transform="rotate(-255.75)"/>
      <use href="#cell-people" class="item" transform="rotate(-265.25)"/>
      <use href="#cell-people" class="item" transform="rotate(-274.75)"/>
      <use href="#cell-people" class="item" transform="rotate(-284.25)"/>
    </g>
    <g class="labels">
      <text class="item-label" transform="rotate(-56.75)" x="-478" dy=".35em" text-anchor="middle">Rostering</text>
      <text class="item-label" transform="rotate(-66.25)" x="-478" dy=".35em" text-anchor="middle">Capability Development</text>
      <text class="item-label" transform="rotate(-75.75)" x="-478" dy=".35em" text-anchor="middle">Culture</text>
      <text class="item-label" transform="rotate(-85.25)" x="-478" dy=".35em" text-anchor="middle">Recruitment And Retention</text>
      <text class="item-label" transform="rotate(-274.75)" x="478" dy=".35em" text-anchor="middle">Wellbeing</text>
      <text class="item-label" transform="rotate(-284.25)" x="478" dy=".35em" text-anchor="middle">Communication And Engagement</text>
    </g>

    <!-- Systems policies procedures -->
    <g class="group f-systems">
      <use href="#cell-systems" class="item" transform="rotate(-295.9)"/>
      <use href="#cell-systems" class="item" transform="rotate(-305.8)"/>
      <use href="#cell-systems" class="item" transform="rotate(-315.6)"/>
      <use href="#cell-systems" class="item" transform="rotate(-325.5)"/>
      <use href="#cell-systems" class="item" transform="rotate(-335.4)"/>
      <use href="#cell-systems" class="item" transform="rotate(-345.2)"/>
      <use href="#cell-systems" class="item" transform="rotate(-355.1)"/>
    </g>
    <g class="labels">
      <text class="item-label" transform="rotate(-295.9)" x="478" dy=".35em" text-anchor="middle">Procedures</text>
      <text class="item-label" transform="rotate(-305.8)" x="478" dy=".35em" text-anchor="middle">Payroll</text>
      <text class="item-label" transform="rotate(-315.6)" x="478" dy=".35em" text-anchor="middle">ICT</text>
      <text class="item-label" transform="rotate(-325.5)" x="478" dy=".35em" text-anchor="middle">Account Payable / Recieveable</text>
      <text class="item-label" transform="rotate(-335.4)" x="478" dy=".35em" text-anchor="middle">Policies</text>
      <text class="item-label" transform="rotate(-345.2)" x="478" dy=".35em" text-anchor="middle">Statutoly Compliance</text>
      <text class="item-label" transform="rotate(-355.1)" x="478" dy=".35em" text-anchor="middle">Financial Planning</text>
    </g>

    <!-- group brackets -->
    <g class="brackets">
      <circle r="340" pathLength="360" class="bracket s-attraction" stroke-dasharray="37.7 400" transform="rotate(-126)"/>
      <circle r="340" pathLength="360" class="ticks s-attraction" stroke-dasharray="0.4 4.986 0.4 4.986 0.4 4.986 0.4 4.986 0.4 4.986 0.4 4.986 0.4 4.986 0.4 400" transform="rotate(-126)"/>
      <circle r="340" pathLength="360" class="bracket s-delivery" stroke-dasharray="40.6 400" transform="rotate(-86.6)"/>
      <circle r="340" pathLength="360" class="ticks s-delivery" stroke-dasharray="0.4 5.4 0.4 5.4 0.4 5.4 0.4 5.4 0.4 5.4 0.4 5.4 0.4 5.4 0.4 400" transform="rotate(-86.6)"/>
      <circle r="340" pathLength="360" class="bracket s-planning" stroke-dasharray="45 400" transform="rotate(-45)"/>
      <circle r="340" pathLength="360" class="ticks s-planning" stroke-dasharray="0.4 5.225 0.4 5.225 0.4 5.225 0.4 5.225 0.4 5.225 0.4 5.225 0.4 5.225 0.4 5.225 0.4 400" transform="rotate(-45)"/>
      <circle r="340" pathLength="360" class="bracket s-commercial" stroke-dasharray="30 400" transform="rotate(-158)"/>
      <circle r="340" pathLength="360" class="ticks s-commercial" stroke-dasharray="0.4 5.6 0.4 5.6 0.4 5.6 0.4 5.6 0.4 5.6 0.4 400" transform="rotate(-158)"/>
      <circle r="340" pathLength="360" class="bracket s-marketing" stroke-dasharray="21 400" transform="rotate(-180)"/>
      <circle r="340" pathLength="360" class="ticks s-marketing" stroke-dasharray="0.4 4.85 0.4 4.85 0.4 4.85 0.4 4.85 0.4 400" transform="rotate(-180)"/>
      <circle r="340" pathLength="360" class="bracket s-assets" stroke-dasharray="50 400" transform="rotate(-230)"/>
      <circle r="340" pathLength="360" class="ticks s-assets" stroke-dasharray="0.4 9.6 0.4 9.6 0.4 9.6 0.4 9.6 0.4 9.6 0.4 400" transform="rotate(-230)"/>
      <circle r="340" pathLength="360" class="bracket s-people" stroke-dasharray="57 400" transform="rotate(-289)"/>
      <circle r="340" pathLength="360" class="ticks s-people" stroke-dasharray="0.4 9.1 0.4 9.1 0.4 9.1 0.4 9.1 0.4 9.1 0.4 9.1 0.4 400" transform="rotate(-289)"/>
      <circle r="340" pathLength="360" class="bracket s-systems" stroke-dasharray="69 400" transform="rotate(-360)"/>
      <circle r="340" pathLength="360" class="ticks s-systems" stroke-dasharray="0.4 9.457 0.4 9.457 0.4 9.457 0.4 9.457 0.4 9.457 0.4 9.457 0.4 9.457 0.4 400" transform="rotate(-360)"/>
    </g>

    <!-- business units -->
    <g class="units">
      <path class="wedge f-planning" d="M0,0 L318,0 L257.27,-186.92 Z"/>
      <path class="wedge f-delivery" d="M0,0 L257.27,-186.92 L98.27,-302.45 Z"/>
      <path class="wedge f-attraction" d="M0,0 L98.27,-302.45 L-98.27,-302.45 Z"/>
      <path class="wedge f-commercial" d="M0,0 L-98.27,-302.45 L-257.27,-186.92 Z"/>
      <path class="wedge f-marketing" d="M0,0 L-257.27,-186.92 L-318,0 Z"/>
      <path class="wedge f-assets" d="M0,0 L-318,0 A318 318 0 0 0 -159,275.4 Z"/>
      <path class="wedge f-people" d="M0,0 L-159,275.4 A318 318 0 0 0 159,275.4 Z"/>
      <path class="wedge f-systems" d="M0,0 L159,275.4 A318 318 0 0 0 318,0 Z"/>
    </g>
    <g class="unit-labels">
      <text class="wedge-label"><tspan x="0" y="-255">Event</tspan><tspan x="0" y="-232">Attraction</tspan><tspan x="0" y="-210">Sales</tspan></text>
      <text class="wedge-label"><tspan x="137" y="-205">Event</tspan><tspan x="137" y="-183">Delivery /</tspan><tspan x="137" y="-160">Operations</tspan></text>
      <text class="wedge-label"><tspan x="226" y="-74">Event Planning</tspan><tspan x="226" y="-52">Management</tspan></text>
      <text class="wedge-label dark" x="-132" y="-175">Commercial</text>
      <text class="wedge-label"><tspan x="-225" y="-88">Marketing</tspan><tspan x="-225" y="-66">And</tspan><tspan x="-225" y="-43">Communications</tspan></text>
      <text class="wedge-label dark"><tspan x="-200" y="87">Assets And</tspan><tspan x="-200" y="109">Facilities</tspan><tspan x="-200" y="131">Managements</tspan></text>
      <text class="wedge-label"><tspan x="0" y="216">People</tspan><tspan x="0" y="238">And</tspan><tspan x="0" y="261">Culture</tspan></text>
      <text class="wedge-label"><tspan x="217" y="77">Systems</tspan><tspan x="217" y="99">Policies</tspan><tspan x="217" y="121">Procedures</tspan></text>
    </g>

    <!-- core -->
    <circle r="160" fill="var(--paper)"/>
    <g class="pointers">
      <use href="#pointer" class="f-attraction" transform="rotate(-90)"/>
      <use href="#pointer" class="f-commercial" transform="rotate(-127)"/>
      <use href="#pointer" class="f-gold" transform="rotate(-53)"/>
      <use href="#pointer" class="f-marketing" transform="rotate(-164)"/>
      <use href="#pointer" class="f-marketing" transform="rotate(-17)"/>
      <use href="#pointer" class="f-systems" transform="rotate(32)"/>
      <use href="#pointer" class="f-people" transform="rotate(90)"/>
      <use href="#pointer" class="f-assets-arrow" transform="rotate(149)"/>
    </g>

    <g class="cycle">
      <circle r="127" pathLength="360" class="ring" stroke-dasharray="22 400" transform="rotate(-125)"/>
      <circle r="127" pathLength="360" class="ring" stroke-dasharray="19 400" transform="rotate(-77)"/>
      <circle r="127" pathLength="360" class="ring" stroke-dasharray="40 400" transform="rotate(-22)"/>
      <circle r="127" pathLength="360" class="ring" stroke-dasharray="23 400" transform="rotate(52)"/>
      <circle r="127" pathLength="360" class="ring" stroke-dasharray="23 400" transform="rotate(105)"/>
      <circle r="127" pathLength="360" class="ring" stroke-dasharray="40 400" transform="rotate(162)"/>
      <use href="#cycle-arrow" transform="rotate(-103)"/>
      <use href="#cycle-arrow" transform="rotate(-58)"/>
      <use href="#cycle-arrow" transform="rotate(18)"/>
      <use href="#cycle-arrow" transform="rotate(75)"/>
      <use href="#cycle-arrow" transform="rotate(128)"/>
      <use href="#cycle-arrow" transform="rotate(202)"/>
      <text class="ring-label" dy="5.5"><textPath href="#cycle-top" startOffset="21.4%" text-anchor="middle">ATTRACT</textPath></text>
      <text class="ring-label" dy="5.5"><textPath href="#cycle-top" startOffset="50%" text-anchor="middle">PLAN</textPath></text>
      <text class="ring-label" dy="5.5"><textPath href="#cycle-top" startOffset="77.8%" text-anchor="middle">DELIVER</textPath></text>
      <text class="ring-label" dy="5.5"><textPath href="#cycle-bottom" startOffset="19.4%" text-anchor="middle">PREPARE</textPath></text>
      <text class="ring-label" dy="5.5"><textPath href="#cycle-bottom" startOffset="50%" text-anchor="middle">ENABELE</textPath></text>
      <text class="ring-label" dy="5.5"><textPath href="#cycle-bottom" startOffset="80.6%" text-anchor="middle">PROTECT</textPath></text>
    </g>

    <g class="hub">
      <path fill="var(--events)" d="M-104,-3 A104 104 0 0 1 104,-3 Z"/>
      <path fill="var(--core)" d="M104,8 A104 104 0 0 1 -104,8 Z"/>
      <line x1="-35" y1="8" x2="-35" y2="110" stroke="var(--paper)" stroke-width="4"/>
      <line x1="35" y1="8" x2="35" y2="110" stroke="var(--paper)" stroke-width="4"/>
      <text class="events-label" x="0" y="-8">EVENTS</text>
      <text class="core-label" transform="translate(-58 42) rotate(90)">VENUES</text>
      <text class="core-label" x="0" y="72">PEOPLE</text>
      <text class="core-label" transform="translate(58 42) rotate(90)">SYSTEMS</text>
    </g>
  </g>
</svg>
</body>
</html>
```